Web Site Design for a Finance (lending) Company

We are opening a new subsidiary that focuses on lending money in the real estate industry. We need a web site designed to represent the business.

The business is lending money to real estate investors. A typical client/borrower will be looking to borrow money to buy a house, renovate it and then sell it at a profit, all within 12 months or less.

Company name is Brevand Finance. Our logo is attached.

Attached is a general outline for the web site. We're working on writing more text for each page but this should give you enough to get started with some ideas.

Competitor web site that I like a lot (as an example): https://quorvelfunding.com/. Many of the general items on this site match what we will need (description of loan programs, FAQ)

Target Market(s)

Real estate investors (generally individuals or small companies with just a few people) who are buying homes, renovating them and then selling them at a profit.

Industry/Entity Type

Finance

Coding

Coded - Design and coding required

Number of Pages Required

5+ page

Colors

Designer to choose colors to be used in the design.

Requirements
Must have
• Minimalist design. Clean lines without too much clutter. Some stock photography is ok but the photos should not be distracting. They should almost fade in to the background so that user can focus on the key information about what our company does instead. We are a finance company, not a design company, so the information about our products will be more interesting to site visitors than the art.
• Some minimalist examples from Snapboard:
• https://www.snapboard-example.com/explore/minimalist-web-design/
Nice to have
• If you search in seekly for "hard money lenders" you will find many examples of web sites from our competition. I have provided a link above to competitor web site that I like a lot.
• I have attached our logo in EPS format. Logo is green. Web site doesn't have to be green but it should be of a color that will work well with the logo.

```html
<!DOCTYPE html>
<html lang="en">
<head>
<meta charset="utf-8">
<title>Brevand Finance — Real Estate Lending</title>
<link rel="stylesheet" href="https://fonts.googleapis.com/css2?family=Roboto:ital,wght@0,300;0,400;0,500;0,700;1,400&display=swap">
<style>
:root{
  --green:#0c5a35;
  --green-dark:#07472a;
  --green-deep:#0a4f30;
  --ink:#333;
  --muted:#666;
  --grey:#9a9a9a;
  --grey-light:#eeeeee;
  --line:#dcdcdc;
  --white:#fff;
  --charcoal:#2e2e2e;
}
*{box-sizing:border-box;margin:0;padding:0}
html,body{width:1200px;height:4534px;overflow:hidden}
body{font-family:"Roboto",Arial,sans-serif;color:var(--ink);background:var(--white);position:relative}
section,header,footer{position:relative;width:1200px;overflow:hidden}
.abs{position:absolute}
.btn{position:absolute;display:flex;align-items:center;justify-content:center;background:var(--green);color:var(--white);font-size:19px;font-weight:500;letter-spacing:.5px;text-transform:uppercase;clip-path:polygon(14px 0,calc(100% - 14px) 0,100% 50%,calc(100% - 14px) 100%,14px 100%,0 50%)}
.photo{position:absolute}
.lorem{font-size:14px;line-height:24px;color:var(--muted)}

/* header */
.site-header{height:166px;background:var(--white)}
.nav-band{position:absolute;left:0;top:100px;width:1200px;height:66px;background:var(--green)}
.brand-plate{position:absolute;left:66px;top:0;width:196px;height:136px;background:var(--white);clip-path:polygon(0 0,100% 0,100% 82%,50% 100%,0 82%);display:flex;align-items:center;gap:12px;padding:0 0 18px 18px;box-shadow:0 2px 6px rgba(0,0,0,.2)}
.brand-mark{width:22px;height:22px;background:var(--green);flex:none}
.brand-name{font-size:22px;font-weight:500;color:var(--green);line-height:26px}
.call{position:absolute;left:665px;top:22px;display:flex;align-items:center;gap:12px}
.call small{display:block;font-size:13px;color:var(--muted)}
.call strong{display:block;font-size:30px;font-weight:500;color:var(--green-dark);line-height:32px}
.quote{left:916px;top:24px;width:202px;height:55px;font-size:20px;font-weight:400}
.main-nav{position:absolute;top:100px;left:529px;display:flex;height:66px}
.main-nav a{color:var(--white);text-decoration:none;font-size:15px;display:flex;align-items:center;padding:0 22px}
.main-nav a.active{background:#9d9d9d}

/* hero */
.hero{height:514px}
.hero-photo{left:0;top:0;width:1200px;height:514px;background:linear-gradient(100deg,#8e8c86 0%,#c9c3b6 45%,#a9a39a 70%,#6f6d68 100%)}
.hero-shade{position:absolute;inset:0;background:rgba(40,40,40,.35)}
.hero h1{position:absolute;left:0;top:128px;width:1200px;text-align:center;color:var(--white);font-size:44px;font-weight:500;line-height:54px;text-transform:uppercase;letter-spacing:.5px}
.hero p{position:absolute;left:0;top:250px;width:1200px;text-align:center;color:var(--white);font-size:15px;line-height:22px}
.hero .cta{left:502px;top:333px;width:196px;height:54px}
.slide-arrow{position:absolute;top:228px;width:40px;height:40px;background:var(--green);display:flex;align-items:center;justify-content:center}

/* features */
.features{height:293px;background:var(--grey-light)}
.feature{position:absolute;top:0;width:398px;height:293px;text-align:center}
.feature .icon{position:absolute;left:0;right:0;top:44px;margin:auto;width:72px;height:72px}
.feature h3{position:absolute;top:132px;width:100%;font-size:17px;font-weight:400;color:var(--green);text-transform:uppercase}
.feature p{position:absolute;top:162px;left:36px;right:36px;font-size:14px;line-height:24px;color:var(--muted)}
.feature.focus{left:402px;top:0;width:399px;background:var(--green);border:3px solid var(--white);outline:1px solid var(--green);outline-offset:-8px}
.feature.focus h3,.feature.focus p{color:var(--white)}

/* welcome */
.welcome{height:454px;text-align:center}
.eyebrow{font-size:19px;color:var(--ink);text-transform:uppercase;font-weight:400}
.section-title{font-size:40px;font-weight:300;text-transform:uppercase;color:#555}
.welcome .eyebrow{position:absolute;top:82px;width:100%}
.welcome .section-title{position:absolute;top:108px;width:100%}
.welcome .lorem{position:absolute;left:160px;width:880px;text-align:center}
.welcome .more{left:502px;top:336px;width:196px;height:52px}

/* loan program */
.loans{height:571px;background:linear-gradient(90deg,#3a3a3a,#1f1f1f)}
.loans-bg{left:0;top:0;width:1200px;height:571px;background:linear-gradient(180deg,#4a4a4a 0%,#2a2a2a 60%,#1d1d1d 100%)}
.advisor{left:60px;top:64px;width:363px;height:507px;background:linear-gradient(180deg,#b9a48e 0%,#2b2f3a 40%,#23262e 100%);border-radius:160px 160px 0 0}
.loans .section-title{position:absolute;left:640px;top:88px;color:#e6e6e6;font-size:42px}
.loan-card{position:absolute;top:169px;width:317px;height:339px;background:rgba(120,120,120,.55)}
.loan-card .photo{left:0;top:0;width:317px;height:181px}
.loan-card h4{position:absolute;top:200px;width:100%;text-align:center;color:var(--white);font-size:17px;font-weight:400;text-transform:uppercase}
.loan-card p{position:absolute;top:228px;left:30px;right:30px;text-align:center;color:#e8e8e8;font-size:14px;line-height:23px}
.loan-card .btn{left:58px;top:308px;width:200px;height:56px}

/* blog */
.blog{height:608px;text-align:center}
.blog .eyebrow{position:absolute;top:60px;width:100%;color:var(--green)}
.blog .section-title{position:absolute;top:88px;width:100%}
.post{position:absolute;top:169px;width:322px;height:372px;background:var(--white);box-shadow:0 1px 5px rgba(0,0,0,.25);text-align:left}
.post .photo{left:0;top:0;width:322px;height:198px}
.date{position:absolute;left:10px;top:212px;width:76px}
.date span{display:block;background:var(--green);color:var(--white);font-size:16px;text-align:center;height:28px;line-height:28px}
.date b{display:block;background:#8e8e8e;color:var(--white);font-size:36px;font-weight:300;text-align:center;height:56px;line-height:56px}
.post h5{position:absolute;left:104px;top:214px;font-size:16px;font-weight:500;color:#222}
.post .by{position:absolute;left:104px;top:244px;font-size:13px;color:var(--muted);display:flex;gap:8px;align-items:center}
.post .by b{color:var(--green)}
.post p{position:absolute;left:104px;top:272px;right:16px;font-size:14px;line-height:22px;color:var(--muted)}

/* team */
.team{height:456px;background:var(--green)}
.team-low{left:0;top:265px;width:1200px;height:191px;background:#a3a3a3}
.team .section-title{position:absolute;top:60px;width:100%;text-align:center;color:#d9d9d9;font-size:40px}
.team .section-title strong{font-weight:400;color:var(--white)}
.member{position:absolute;top:145px;width:477px;height:251px;background:var(--white);box-shadow:0 3px 10px rgba(0,0,0,.3)}
.member .portrait{position:absolute;left:28px;top:30px;width:150px;height:150px;background:linear-gradient(160deg,#c7bfb6,#8f857d);clip-path:polygon(0 0,100% 0,100% 62%,50% 100%,0 62%)}
.member .frame{position:absolute;left:10px;top:20px}
.member h4{position:absolute;left:224px;top:48px;font-size:19px;font-weight:400;color:#555}
.member p{position:absolute;left:224px;top:82px;right:28px;font-size:14px;line-height:23px;color:var(--muted)}
.member .socials{position:absolute;left:224px;top:166px;display:flex;gap:10px}
.member .socials i{width:28px;height:26px;border:2px solid var(--green);display:block}
.member .read{position:absolute;right:28px;top:218px;font-size:15px;color:var(--green);text-decoration:underline}

/* testimonials */
.testimonials{height:566px;text-align:center}
.testi-bg{left:0;top:0;width:1200px;height:566px;background:linear-gradient(120deg,#ededed 0%,#d8d8d8 40%,#f2f2f2 70%,#e2e2e2 100%)}
.testi-veil{position:absolute;inset:0;background:rgba(255,255,255,.55)}
.testimonials .eyebrow{position:absolute;top:66px;width:100%;color:#444;font-size:20px}
.testimonials .section-title{position:absolute;top:92px;width:100%;font-size:40px}
.avatar{position:absolute;left:529px;top:160px;width:142px;height:142px;border-radius:50%;border:4px solid var(--green);background:var(--white);padding:6px}
.avatar div{width:100%;height:100%;border-radius:50%;background:linear-gradient(160deg,#d4cbc0,#8e8178)}
.testimonials .quote-text{position:absolute;left:160px;width:880px;top:344px;font-size:15px;line-height:25px;color:#444}
.client{position:absolute;top:434px;width:100%;display:flex;justify-content:center;align-items:center;gap:12px;font-size:16px;font-weight:500;color:var(--green);text-transform:uppercase}
.client::before{content:"";width:34px;height:4px;background:var(--green)}
.client-role{position:absolute;top:462px;width:100%;font-size:13px;color:var(--grey)}
.chev{position:absolute;top:340px}
.live-chat{position:absolute;left:1152px;top:188px;width:48px;height:181px;background:#7d7d7d;color:var(--white);display:flex;flex-direction:column;align-items:center;justify-content:flex-end;border-radius:6px 0 0 6px}
.live-chat span{writing-mode:vertical-rl;transform:rotate(180deg);font-size:16px;letter-spacing:1px;margin-bottom:18px}
.live-chat i{width:48px;height:40px;background:var(--green);display:block;border-radius:0 0 0 6px}

/* membership */
.membership{height:350px;text-align:center}
.membership .section-title{position:absolute;top:58px;width:100%;font-size:40px;color:var(--green);font-weight:400}
.membership .section-title span{color:#8a8a8a;font-weight:300}
.badges{position:absolute;top:130px;left:76px;display:flex;gap:13px}
.badge{width:200px;height:118px;background:var(--white);box-shadow:0 1px 6px rgba(0,0,0,.25);display:flex;align-items:center;justify-content:center}
.badge.current{border:4px solid #9fc5b3}
.badge i{display:block;width:120px;height:34px;background:#c9d3cf;border-radius:4px}
.dots{position:absolute;top:276px;left:563px;display:flex;gap:12px}
.dots i{width:16px;height:16px;border-radius:50%;border:2px solid #999;display:block}
.dots i.on{background:var(--green);border-color:var(--green)}

/* footer */
.site-footer{height:556px;background:var(--green)}
.footer-left{left:0;top:0;width:469px;height:499px;background:linear-gradient(160deg,#3e3e3e,#262626)}
.footer-left-veil{left:0;top:0;width:469px;height:499px;background:rgba(8,50,30,.35)}
.site-footer h4{position:absolute;font-size:20px;font-weight:400;color:#d5d5d5;text-transform:uppercase}
.site-footer .note{position:absolute;left:78px;top:86px;font-size:14px;font-style:italic;color:#e0e0e0}
.field{position:absolute;left:78px;width:352px;height:40px;border:1px solid rgba(255,255,255,.5);background:rgba(0,0,0,.2);color:#e6e6e6;font-size:14px;padding:11px 12px}
.submit{left:78px;top:380px;width:200px;height:54px}
.links{position:absolute;left:534px;top:130px;list-style:none}
.links li{font-size:15px;color:#e4e4e4;line-height:30px;display:flex;align-items:center;gap:18px}
.links li::before{content:"";width:8px;height:8px;background:#bcd6c9}
.follow{position:absolute;left:514px;top:292px;font-size:19px;color:#d5d5d5}
.social-row{position:absolute;left:514px;top:335px;display:flex;gap:12px}
.social-row i{width:40px;height:40px;border-radius:50%;background:#5f8b75;display:block}
.touch{position:absolute;left:816px;display:flex;gap:22px;color:#e6e6e6;font-size:14px;line-height:22px}
.touch .ic{width:58px;height:58px;background:#6a8f7e;flex:none;display:flex;align-items:center;justify-content:center}
.touch b{display:block;font-size:16px;font-weight:500;color:var(--white)}
.copyright{position:absolute;left:0;top:499px;width:1200px;height:57px;background:#7a7a7a;color:#eee;font-size:14px;display:flex;align-items:center;justify-content:center}
.copyright b{color:#cde3d7;font-weight:500;margin-right:6px}
</style>
</head>
<body>

<header class="site-header">
  <div class="nav-band"></div>
  <div class="brand-plate"><span class="brand-mark"></span><span class="brand-name">Brevand<br>Finance</span></div>
  <div class="call">
    <svg width="38" height="38" viewBox="0 0 24 24"><path fill="#0c5a35" d="M6.6 10.8a15.1 15.1 0 0 0 6.6 6.6l2.2-2.2a1 1 0 0 1 1-.25 11.4 11.4 0 0 0 3.6.57 1 1 0 0 1 1 1V20a1 1 0 0 1-1 1A17 17 0 0 1 3 4a1 1 0 0 1 1-1h3.5a1 1 0 0 1 1 1c0 1.25.2 2.45.57 3.6a1 1 0 0 1-.25 1z"/></svg>
    <div><small>Call Us Today :</small><strong>123 456 7890</strong></div>
  </div>
  <div class="btn quote">Get a Quote</div>
  <nav class="main-nav">
    <a class="active" href="#">HOME</a><a href="#">ABOUT US</a><a href="#">LOANS</a><a href="#">RESOURCES</a><a href="#">CONTACT US</a>
  </nav>
</header>

<section class="hero">
  <div class="photo hero-photo" role="img" aria-label="Hands passing a small model house over property paperwork"></div>
  <div class="hero-shade"></div>
  <h1>Local real estate experts lending to<br>local real estate investors</h1>
  <p>Brevand Finance is a local business with local knowledge and strong industry relationships. A partner with a wide<br>network who offers value-added services</p>
  <div class="btn cta">Contact Us</div>
  <div class="slide-arrow" style="left:12px"><svg width="14" height="14" viewBox="0 0 10 10"><path d="M7 1 3 5l4 4" stroke="#fff" stroke-width="2" fill="none"/></svg></div>
  <div class="slide-arrow" style="right:12px"><svg width="14" height="14" viewBox="0 0 10 10"><path d="M3 1l4 4-4 4" stroke="#fff" stroke-width="2" fill="none"/></svg></div>
</section>

<section class="features">
  <div class="feature" style="left:20px">
    <svg class="icon" viewBox="0 0 72 72"><circle cx="34" cy="38" r="26" fill="none" stroke="#8a8a8a" stroke-width="5"/><circle cx="34" cy="38" r="15" fill="none" stroke="#8a8a8a" stroke-width="5"/><circle cx="34" cy="38" r="5" fill="#8a8a8a"/><path d="M34 38 62 10M54 8h10v10" stroke="#8a8a8a" stroke-width="4" fill="none"/></svg>
    <h3>Mission</h3>
    <p>Lorem Ipsum is simply dummy text of the printing and typesetting industry. Lorem Ipsum has been the industry's standard dummy</p>
  </div>
  <div class="feature focus">
    <svg class="icon" viewBox="0 0 72 72"><circle cx="36" cy="36" r="24" fill="none" stroke="#fff" stroke-width="4"/><circle cx="36" cy="36" r="12" fill="none" stroke="#fff" stroke-width="4"/><path d="M36 4v22M36 46v22M4 36h22M46 36h22" stroke="#fff" stroke-width="4"/></svg>
    <h3>Focus</h3>
    <p>Lorem Ipsum is simply dummy text of the printing and typesetting industry. Lorem Ipsum has been the industry's standard dummy</p>
  </div>
  <div class="feature" style="left:800px">
    <svg class="icon" viewBox="0 0 72 72"><rect x="10" y="48" width="9" height="18" fill="#8a8a8a"/><rect x="24" y="38" width="9" height="28" fill="#8a8a8a"/><rect x="38" y="28" width="9" height="38" fill="#8a8a8a"/><rect x="52" y="18" width="9" height="48" fill="#8a8a8a"/><text x="14" y="30" font-family="Roboto,sans-serif" font-size="26" fill="#8a8a8a">$</text></svg>
    <h3>What makes Brevand different</h3>
    <p>Lorem Ipsum is simply dummy text of the printing and typesetting industry. Lorem Ipsum has been the industry's standard dummy</p>
  </div>
</section>

<section class="welcome">
  <div class="eyebrow">Welcome to</div>
  <h2 class="section-title">Brevand Finance</h2>
  <p class="lorem" style="top:174px">Lorem Ipsum is simply dummy text of the printing and typesetting industry. Lorem Ipsum has been the industry's standard dummy text ever since the 1500s, when an unknown printer took a galley of type and scrambled.</p>
  <p class="lorem" style="top:234px">Lorem Ipsum is simply dummy text of the printing and typesetting industry. Lorem Ipsum has been the industry's standard dummy text ever since the 1500s, when an unknown printer took a galley of type and scrambled it to make a type specimen book. It has survived not only five centuries, but also the leap into electronic typesetting, remaining essentially unchanged.</p>
  <div class="btn more">Learn More</div>
</section>

<section class="loans">
  <div class="photo loans-bg" role="img" aria-label="Dim city skyline behind the loan programs"></div>
  <div class="photo advisor" role="img" aria-label="Smiling loan advisor in a suit offering a handshake"></div>
  <h2 class="section-title">Loan Program</h2>
  <div class="loan-card" style="left:475px">
    <div class="photo" role="img" aria-label="Family meeting a realtor outside a home" style="background:linear-gradient(150deg,#c9d2c4,#8f9a8a)"></div>
    <h4>Fix and Flip Loans</h4>
    <p>Lorem Ipsum is simply dummy text of the printing and typesetting industry.</p>
    <div class="btn">Learn More</div>
  </div>
  <div class="loan-card" style="left:810px">
    <div class="photo" role="img" aria-label="Hand holding keys in front of a commercial building" style="background:linear-gradient(150deg,#dce3ea,#9eabb8)"></div>
    <h4>Commercial Hard Money Loan</h4>
    <p>Lorem Ipsum is simply dummy text of the printing and typesetting industry.</p>
    <div class="btn">Learn More</div>
  </div>
</section>

<section class="blog">
  <div class="eyebrow">Resources</div>
  <h2 class="section-title">Latest Blog</h2>
  <article class="post" style="left:79px">
    <div class="photo" role="img" aria-label="People reviewing documents at a desk" style="background:linear-gradient(150deg,#c7cfd6,#7f8a94)"></div>
    <div class="date"><span>Oct</span><b>03</b></div>
    <h5>Lorem Ipsum is the simply</h5>
    <div class="by"><svg width="12" height="12" viewBox="0 0 12 12"><circle cx="6" cy="4" r="3" fill="#0c5a35"/><path d="M0 12a6 5 0 0 1 12 0z" fill="#0c5a35"/></svg>Posted By <b>Brevand</b></div>
    <p>Lorem Ipsum is simply dummy text of the printing and typesetting industry.</p>
  </article>
  <article class="post" style="left:438px">
    <div class="photo" role="img" aria-label="Couple talking by a waterfront" style="background:linear-gradient(150deg,#b9c6cf,#7b8790)"></div>
    <div class="date"><span>Oct</span><b>03</b></div>
    <h5>Lorem Ipsum is the simply</h5>
    <div class="by"><svg width="12" height="12" viewBox="0 0 12 12"><circle cx="6" cy="4" r="3" fill="#0c5a35"/><path d="M0 12a6 5 0 0 1 12 0z" fill="#0c5a35"/></svg>Posted By <b>Brevand</b></div>
    <p>Lorem Ipsum is simply dummy text of the printing and typesetting industry.</p>
  </article>
  <article class="post" style="left:798px">
    <div class="photo" role="img" aria-label="Couple touring an empty bright room" style="background:linear-gradient(150deg,#e4e4e2,#a7a6a2)"></div>
    <div class="date"><span>Oct</span><b>03</b></div>
    <h5>Lorem Ipsum is the simply</h5>
    <div class="by"><svg width="12" height="12" viewBox="0 0 12 12"><circle cx="6" cy="4" r="3" fill="#0c5a35"/><path d="M0 12a6 5 0 0 1 12 0z" fill="#0c5a35"/></svg>Posted By <b>Brevand</b></div>
    <p>Lorem Ipsum is simply dummy text of the printing and typesetting industry.</p>
  </article>
</section>

<section class="team">
  <div class="abs team-low"></div>
  <h2 class="section-title">Meet our <strong>Team</strong></h2>
  <div class="member" style="left:109px">
    <div class="portrait" role="img" aria-label="Team member portrait"></div>
    <svg class="frame" width="170" height="180" viewBox="0 0 170 180"><path d="M4 110 85 176 166 110" stroke="#0c5a35" stroke-width="6" fill="none"/></svg>
    <h4>NORA</h4>
    <p>Lorem Ipsum is simply dummy text of the printing and type setting the industry Lorem Ipsum is.</p>
    <div class="socials"><i></i><i></i><i></i></div>
    <span class="read">Read More...</span>
  </div>
  <div class="member" style="left:608px">
    <div class="portrait" role="img" aria-label="Team member portrait"></div>
    <svg class="frame" width="170" height="180" viewBox="0 0 170 180"><path d="M4 110 85 176 166 110" stroke="#0c5a35" stroke-width="6" fill="none"/></svg>
    <h4>ELLIS</h4>
    <p>Lorem Ipsum is simply dummy text of the printing and type setting the industry Lorem Ipsum is.</p>
    <div class="socials"><i></i><i></i><i></i></div>
    <span class="read">Read More...</span>
  </div>
</section>

<section class="testimonials">
  <div class="photo testi-bg" role="img" aria-label="Faded image of a hand signing a contract beside a model house"></div>
  <div class="testi-veil"></div>
  <div class="eyebrow">Testimonials</div>
  <h2 class="section-title">What our client say</h2>
  <div class="avatar"><div role="img" aria-label="Client portrait"></div></div>
  <svg class="chev" style="left:142px" width="18" height="50" viewBox="0 0 18 50"><path d="M16 2 2 25l14 23" stroke="#555" stroke-width="2" fill="none"/></svg>
  <svg class="chev" style="left:1040px" width="18" height="50" viewBox="0 0 18 50"><path d="M2 2l14 23L2 48" stroke="#555" stroke-width="2" fill="none"/></svg>
  <p class="quote-text">Lorem Ipsum is simply dummy text of the printing and typesetting industry. Lorem Ipsum has been the industry's standard dummy text ever since the 1500s, when an unknown printer took a galley of type and scrambled it to make a type specimen book. It has survived not only five centuries, but also the leap.</p>
  <div class="client">Client Name</div>
  <div class="client-role">something.com</div>
  <div class="live-chat"><span>LIVE CHAT</span><i></i></div>
</section>

<section class="membership">
  <h2 class="section-title">Industry <span>Membership</span></h2>
  <div class="badges">
    <div class="badge current"><i></i></div>
    <div class="badge"><i></i></div>
    <div class="badge"><i></i></div>
    <div class="badge"><i></i></div>
    <div class="badge"><i></i></div>
  </div>
  <div class="dots"><i></i><i></i><i class="on"></i></div>
</section>

<footer class="site-footer">
  <div class="photo footer-left" role="img" aria-label="Dark city buildings behind the contact form"></div>
  <div class="abs footer-left-veil"></div>
  <h4 style="left:78px;top:48px">Contact Us</h4>
  <p class="note">Need a free quote, or have a question? Get in touch!</p>
  <div class="field" style="top:124px">First Name*</div>
  <div class="field" style="top:172px">Last Name*</div>
  <div class="field" style="top:220px">Email *</div>
  <div class="field" style="top:268px">Phone *</div>
  <div class="field" style="top:316px">How you heard about us *</div>
  <div class="btn submit">Submit</div>

  <h4 style="left:514px;top:48px">Usefull Links</h4>
  <ul class="links"><li>Home</li><li>About Us</li><li>Loans</li><li>Resources</li><li>Contact Us</li></ul>
  <div class="follow">Follow Us On :</div>
  <div class="social-row"><i></i><i></i><i></i></div>

  <h4 style="left:819px;top:48px">Get in Touch</h4>
  <div class="touch" style="top:118px">
    <div class="ic"><svg width="22" height="28" viewBox="0 0 22 28"><path d="M11 0a11 11 0 0 0-11 11c0 8 11 17 11 17s11-9 11-17A11 11 0 0 0 11 0z" fill="#fff"/><circle cx="11" cy="11" r="4" fill="#6a8f7e"/></svg></div>
    <div><b>BREVAND FINANCE</b>Lorem Ipsum is simply dummy text<br>of the printing and typesetting<br>industry.</div>
  </div>
  <div class="touch" style="top:236px;align-items:center">
    <div class="ic"><svg width="26" height="26" viewBox="0 0 24 24"><path fill="#fff" d="M6.6 10.8a15.1 15.1 0 0 0 6.6 6.6l2.2-2.2a1 1 0 0 1 1-.25 11.4 11.4 0 0 0 3.6.57 1 1 0 0 1 1 1V20a1 1 0 0 1-1 1A17 17 0 0 1 3 4a1 1 0 0 1 1-1h3.5a1 1 0 0 1 1 1c0 1.25.2 2.45.57 3.6a1 1 0 0 1-.25 1z"/></svg></div>
    <div><b>123 456 7890</b></div>
  </div>
  <div class="touch" style="top:322px;align-items:center">
    <div class="ic"><svg width="28" height="20" viewBox="0 0 28 20"><rect x="1" y="1" width="26" height="18" fill="#fff"/><path d="M1 1l13 10L27 1" stroke="#6a8f7e" stroke-width="2" fill="none"/></svg></div>
    <div>info@brevandfinance.com</div>
  </div>

  <div class="copyright"><b>©Brevand Finance</b> 2017 All Right Reserved</div>
</footer>

</body>
</html>
```